Guarenteed! - Homepage Website Design - Coding not required- Winner to complete further pages

Hi all,

We're looking at redesigning our current website with a few adjustments to other pages but the main adjustments will be on the homepage which is what this design request is for. Please note : any of these ideas can be changed if you have something particularly different / special in mind etc.

P.S Coding is not required, just a design.

- Our website -

Our website is simply a price comparison website that allows customers to find companies within their area at the best price. The products available are mostly related to the vehicle trade and all refer to vinyl. This includes the likes of vehicle window tint, vehicle colour change vehicle wrap, vehicle signage as well as other cosmetic vinyl modifications. We allow the customer to search for their product within their chosen area and receive a list of companies who supply their product within that area. From here they can compare prices and view further details on the company.

- What we're looking to do -

We're looking first of all to adjust how the website homepage is displayed, this includes adding images and adjusting the colours that are explained below:

First of all, we look to spread out each of the 12 products (which can be seen on the website as it stands) and add an image to each of the products (all being spaced out as shown in our sketch)

We've been told the website looks too busy so we're thinking if we adjust the colours to more simplier neutral colours as well as the main focus of the website being on the 12 images, that would be great.

- Logo + Banner -

Logo to remain top left although banner may be removed / adjusted to make simplier.

- Colours -

Adjustments - Colours shades
We want the website to still look exciting but simplify the colours. Needs to be kept up to date with the colours / textures etc (bright colours to highlight keypoints)
We're still looking to use either blue or orange or maybe both to highlight these keypoints but the main website to be light colours and maybe even black on white background. The entire homepage can be adjusted colour wise if you feel it fits into your theme including menu bars, banners etc. The key is to get this right with being not too overpowering with the colours but still look interesting and up to date.

- 1 - 4 steps banner - (text may change)

This sits just under the logo and explains to the user how easy the website is to use and the steps they need to take. This may change to a 1 - 5 steps but we're looking to have this designed once the overall colours / theme of the website is sorted.

- 12 images - 4 x 3

This is the main focus of the website and will be the main focus of what the customer sees first of all. This will be where they select their product and then underneath, enter their postcode and distance they would like to search within. As explained further up, we have some of the product images available so if you can where possible add these to the design and then duplicate the images on those we currently don't have available.

- 12 Images -Titles -

These titles will be in this order from left to right and etc

- Colour Change Wrap
- Printed Vehicle Wrap
- Window Tint
- Headlight Tint
- Vehicle Signage
- Shop Signage
- Roof Vinyl Wrap
- Bonnet Vinyl Wrap
- Carbon Fibre Vinyl
- Stickerbomb Vinyl
- Clear Protective Vinyl
- Wheel Refurb

Text to be quite large, centered and with the o to the left of the title. Short titles like 'Window Tint' should fit on one line in the middle of the box where as titles such as ' Stickerbomb Vinyl Wrap' should have the 'Stickerbomb Vinyl' on the first line with the 'Wrap' on the line below. The background of this text is up to experient, might be worth just a simple colour or it might be worth using a bright blue or orange to keep in with the theme of the logo etc.

These will also have the circle tick box to the left of the title (as on the current website) where the customer clicks to select the product they have available.
We were also thinking that if when the customer ticks the circle on their selected box, the box is highlighted in some way to show this.

- Search Block -

This will appear under the 12 images and allows the customer to input their postcode and distance for the search criteria. Colours on this can of course be adjusted to keep in theme with the website.

- Under the 12 Images -

- Block underneath the 12 images and search block -

To the left will be some key bullet points about the website - maybe 4 or 5 with a green tick to the left of this. Background colour will probably be best to be a light colour, possibly grey.

Then to the right of this will appear 4 images, 2 before and 2 after when applying these products. Images to be used aren't fully decided on and we would like this stage of the design left to the end when the rest of the theme etc have been decided on.

Attached images are as follows :
- How the website looks as it stands
- The fold line on the website (obviously important)
- Our rough sketch of how we'd like the website homepage to look.
- We have 7 of the images ready that are all attached in this one file. Please duplicate the images on those that currently don't have the image available.

We will also be requesting a website developer to put this into action if our current designer falls through so please feel free to contact us if potentially interested.

The layout can change if you can think of something particular different / unique that works with this design. The main idea is to not only get the 12 products on view to the viewers but also the keypoints and before and after images.

Any questions, please ask away as we're bound to have forgotten a few things.

Thanks and good luck!

Hi all, keep the designs coming.

We haven't quite seen that extra special design we're after. As stated, we're after something fairly simple to suit the youth as well as the middle aged but we're also after something that bit special.

Colours to concentrate on are still and orange etc although feel free to use other colours if you have anything special in mind.

Please experience and we'll give you our honest feedback.

Many thanks all and good luck!

Hi all, this is a message to all the designers.

Some good designs coming in but we're still after that something special for the website design. Keep the designs coming and please feel free to experiment with the design colours, layout etc.

The basic principle of the website needs to remain regarding the 12 products, search within block and 4 steps all appearing on the homepage.

The 4 steps seems to work best when it's got text as well as some simple images next to this.

A variation with the product titles with how to display this, some designers have gone with a simple white background whereas others have gone with colours. Please experiment here and where possible, add a contract / texture to the colour. Please remember the product titles needs to be clear, centured and with the circle tick box to the left of it. 

We're after a fairly simple design although we need it to look 21st century, up to date as well as interesting. The key points straight away are the 4 steps as well as the 12 products so try to guide the viewer to these areas a little.

White background behind the 12 images seems to be a much, although a light colour could possibly work.

The keypoints underneath these 12 products are too very important as it outlines what we do etc. Tick colour can vary.

Next to these keypoints will be the 'before' and 'after' images, these images needs to be fairly small and ensure there is white background around the image itself.

Good luck all and any questions, feel free to ask away.

Thanks!

Hi,

 Thank you for your time and effort with these designs, we are very nearly there with the design but we've thought of something that may work for the homepage. A curved arrow from step 1 pointing to the products, this may or may not work but feel free to give it a go.

Many thanks,

Thank you to everyone for your time and efforts with the design. It's hugely appreciated so thank you all once again.

Wish you all the luck in the future.

```html
<!DOCTYPE html>
<html lang="en">
<head>
<meta charset="utf-8">
<title>VinylScout – Compare Vinyl Installers</title>
<link href="https://fonts.googleapis.com/css2?family=Nunito:ital,wght@0,600;0,700;0,800;1,600;1,700&family=Open+Sans:ital,wght@0,400;0,600;1,400;1,600&display=swap" rel="stylesheet">
<style>
:root{
  --page:#e4e9f1;
  --page-dark:#d6dde9;
  --navy:#2d4a86;
  --navy-dark:#1f3566;
  --blue:#4f77b8;
  --blue-light:#9db8de;
  --orange:#f39a1c;
  --orange-light:#ffd48a;
  --orange-pale:#fff1d0;
  --cream:#fff6dc;
  --text-blue:#33528f;
  --text-orange:#e8860f;
  --white:#ffffff;
  --tick:#9cb82a;
  --note:#fdf3a6;
}
*{box-sizing:border-box;margin:0;padding:0}
html,body{width:775px;height:1200px;overflow:hidden}
body{position:relative;background:linear-gradient(var(--page),var(--page-dark));font-family:"Open Sans",Arial,sans-serif;color:var(--text-blue)}
.abs{position:absolute}

/* header */
.header{left:22px;top:4px;width:728px;height:92px;border:1px solid #c7cfdc;background:var(--white)}
.brand{left:0;top:0;width:330px;height:90px;background:linear-gradient(#ffffff,#e7ebf1)}
.brand-mark{left:22px;top:18px;width:44px;height:44px;border-radius:50%;background:var(--orange)}
.brand-name{left:78px;top:14px;font-family:"Nunito",sans-serif;font-weight:800;font-size:38px;color:var(--navy);letter-spacing:1px}
.brand-tag{left:22px;top:70px;width:290px;height:16px;background:var(--navy);color:var(--white);font-family:"Nunito",sans-serif;font-weight:700;font-size:11px;line-height:16px;text-align:center;letter-spacing:.5px}
.promo{left:330px;top:0;width:397px;height:90px;background:linear-gradient(100deg,#fde3b4,#f9b44c)}
.promo h1{position:absolute;left:20px;top:14px;width:270px;text-align:center;font-family:"Nunito",sans-serif;font-weight:800;font-size:17px;line-height:21px;color:#d4620c}
.promo p{position:absolute;left:20px;top:62px;width:270px;text-align:center;font-style:italic;font-size:13px;color:var(--white)}
.promo-map{left:290px;top:4px;width:102px;height:82px;border-radius:6px;background:radial-gradient(circle at 55% 45%,#ffffff,#f6d7a5)}

/* nav */
.nav{left:22px;top:103px;width:728px;height:34px;border-radius:4px;background:linear-gradient(#5b80c0,var(--navy));display:flex;align-items:center;padding-left:18px}
.nav a{font-family:"Nunito",sans-serif;font-weight:800;font-size:14px;color:var(--white);text-decoration:none;margin-right:30px}
.nav a.current{color:var(--orange-light);border-bottom:2px solid var(--orange-light)}
.list-btn{left:405px;top:5px;width:186px;height:24px;border-radius:12px;background:linear-gradient(#ffffff,#cfdaec);color:var(--navy);font-family:"Nunito",sans-serif;font-style:italic;font-weight:700;font-size:13px;line-height:24px;text-align:center}
.social{top:5px;display:flex;align-items:center;gap:3px;font-size:8px;line-height:9px;color:var(--white);font-weight:600}
.social span.dot{width:22px;height:22px;border-radius:50%;background:var(--blue-light);border:2px solid var(--white)}

/* tabs */
.tab{height:20px;border-radius:8px 8px 0 0;background:linear-gradient(#ffd27e,var(--orange));color:var(--white);font-style:italic;font-size:12px;line-height:20px;padding:0 12px 0 6px;display:flex;align-items:center;gap:6px}
.tab b{width:16px;height:16px;border-radius:50%;background:var(--white);color:var(--orange);font-style:normal;font-size:10px;line-height:16px;text-align:center}

/* steps */
.steps{left:22px;top:170px;width:728px;height:58px;border:1px solid var(--orange-light);background:var(--cream);display:flex}
.step{position:relative;flex:1;border-right:1px solid var(--orange-light);background:linear-gradient(#fffaf0,var(--orange-pale))}
.step:last-child{border-right:0}
.step small{position:absolute;left:3px;top:1px;font-size:9px;color:var(--text-orange);font-style:italic}
.step p{position:absolute;left:12px;top:10px;font-style:italic;font-size:13px;line-height:17px;color:var(--text-orange)}
.step svg{position:absolute;right:14px;top:10px}

/* product grid */
.grid{left:24px;top:237px;width:726px;display:grid;grid-template-columns:repeat(4,167px);column-gap:19px;row-gap:15px}
.tile{height:124px;background:var(--white);border:1px solid #cfd6e2;padding:4px;position:relative}
.tile.selected{border:3px solid var(--orange);padding:2px}
.tile .photo{height:92px;background:linear-gradient(#fbfcfe,#dfe4ea)}
.tile .caption{position:absolute;left:4px;right:4px;bottom:4px;height:22px;background:linear-gradient(#fff0c4,#fbb64a);display:flex;align-items:center;gap:5px;padding-left:12px;font-size:9.5px;color:var(--text-orange);font-weight:600;letter-spacing:.2px}
.tile.selected .caption{left:2px;right:2px;bottom:2px}
.caption i{width:11px;height:11px;border-radius:50%;border:1.5px solid var(--white);background:#f4c27a}
.tile.selected .caption i{background:var(--orange)}

/* search */
.search{left:22px;top:665px;width:728px;height:56px;border:1px solid var(--orange-light);background:linear-gradient(#fffaf0,var(--orange-pale));display:flex}
.search .field{position:relative;flex:1;border-right:1px solid var(--orange-light);display:flex;align-items:center;gap:14px;padding-left:32px;font-size:13px}
.search .field small{position:absolute;left:3px;top:1px;font-size:9px;color:var(--text-orange);font-style:italic}
.input{width:118px;height:20px;border:1px solid var(--orange-light);background:var(--white);font-style:italic;font-size:11px;color:var(--text-orange);padding-left:8px;line-height:18px}
.select{width:116px;height:20px;border:1px solid var(--orange-light);background:var(--orange-pale);font-size:11px;color:var(--text-orange);padding-left:8px;line-height:18px;position:relative;font-style:italic}
.select::after{content:"";position:absolute;right:0;top:0;width:26px;height:18px;background:linear-gradient(#ffd27e,var(--orange))}
.search-btn{width:106px;height:26px;border-radius:13px;background:linear-gradient(#d3e0f2,#8fabd7);color:var(--navy);font-family:"Nunito",sans-serif;font-style:italic;font-weight:800;font-size:14px;line-height:26px;text-align:center;margin-left:72px}
.hint{left:0;top:726px;width:775px;text-align:center;font-size:11px;color:var(--text-orange)}

/* lower section */
.divider{left:18px;top:744px;width:740px;height:5px;background:linear-gradient(var(--orange-light),var(--orange))}
.lower{left:18px;top:749px;width:740px;height:392px;background:linear-gradient(#ffffff,#edf1f7)}
.why-tab{left:267px;top:749px;width:146px;height:26px;border-radius:0 0 6px 6px;background:linear-gradient(#a9c2e6,#7c9fd3);color:var(--white);font-family:"Nunito",sans-serif;font-weight:700;font-size:15px;line-height:26px;text-align:center}
.heading{font-family:"Nunito",sans-serif;font-style:italic;font-weight:700;font-size:16px;color:var(--text-orange);display:flex;align-items:center;gap:5px}
.heading::before{content:"";border-left:7px solid transparent;border-right:7px solid transparent;border-top:10px solid var(--orange)}
.keypoints{left:26px;top:809px;width:300px;list-style:none}
.keypoints li{height:68px;display:flex;align-items:center;gap:10px;font-style:italic;font-size:13px}
.keypoints li.accent{color:var(--text-orange)}
.col-rule{left:330px;top:785px;width:1px;height:345px;background:#c9d1de}
.proof-note{left:348px;top:813px;font-size:11px}
.proof-note u{font-weight:600}
.label{font-size:11px}
.shot{position:absolute;width:187px;height:128px;background:var(--white);border:1px solid #d5dbe5;padding:6px}
.shot .img{height:88px;background:var(--note);color:#e5b54b;font-style:italic;font-size:16px;display:flex;align-items:center;justify-content:center}
.shot .sub{position:absolute;left:6px;right:6px;bottom:6px;height:20px;background:linear-gradient(#fff0c4,#fbb64a);font-size:9px;line-height:20px;text-align:center;color:var(--text-orange)}

/* footer */
.footer{left:18px;top:1147px;width:740px;height:32px;border-radius:3px;background:linear-gradient(#5b80c0,var(--navy));display:flex;align-items:center;padding-left:24px}
.footer a{color:var(--white);text-decoration:none;font-size:11px;margin-right:33px}
.footer .legal{position:absolute;right:18px;font-size:10px;font-style:italic;color:var(--blue-light)}
</style>
</head>
<body>

<header class="abs header">
  <div class="abs brand">
    <span class="abs brand-mark"></span>
    <span class="abs brand-name">VinylScout</span>
    <div class="abs brand-tag">Find and Compare Vinyl Installers</div>
  </div>
  <div class="abs promo">
    <h1>FIND A PROFESSIONAL<br>VINYL INSTALLER TODAY</h1>
    <p>Search &amp; Save Below</p>
    <div class="abs promo-map" role="img" aria-label="Map of the country with location pins under a magnifying glass"></div>
  </div>
</header>

<nav class="abs nav">
  <a href="#" class="current">HOME</a>
  <a href="#">ABOUT US</a>
  <a href="#">CONTACT US</a>
  <a href="#">BLOG</a>
  <div class="abs list-btn">List Your Company Here!</div>
  <div class="abs social" style="left:612px"><span>Like<br>Us</span><span class="dot"></span></div>
  <div class="abs social" style="left:670px"><span>Follow<br>Us</span><span class="dot"></span></div>
</nav>

<div class="abs tab" style="left:22px;top:151px"><b>1</b>Start Comparison Here!</div>
<section class="abs steps">
  <div class="step"><small>1</small><p>Select Your<br>Chosen Product</p>
    <svg width="28" height="36" viewBox="0 0 28 36"><path d="M7 15V10a7 7 0 0 1 14 0v5" fill="none" stroke="#f39a1c" stroke-width="3"/><rect x="2" y="15" width="24" height="20" rx="2" fill="#f39a1c"/></svg></div>
  <div class="step"><small>2</small><p>Input Location<br>&amp; Search</p>
    <svg width="36" height="36" viewBox="0 0 36 36"><circle cx="14" cy="14" r="10" fill="none" stroke="#f39a1c" stroke-width="4"/><line x1="21" y1="21" x2="33" y2="33" stroke="#f39a1c" stroke-width="5" stroke-linecap="round"/></svg></div>
  <div class="step"><small>3</small><p>Compare<br>Firms &amp; Prices</p>
    <svg width="36" height="36" viewBox="0 0 36 36"><rect width="36" height="36" rx="3" fill="#f39a1c"/><path d="M6 28L14 18L20 23L30 9" fill="none" stroke="#fff" stroke-width="2.5"/><circle cx="30" cy="9" r="2.5" fill="#fff"/></svg></div>
  <div class="step"><small>4</small><p>Contact Your<br>Chosen Company</p>
    <svg width="22" height="38" viewBox="0 0 22 38"><rect x="1" y="1" width="20" height="36" rx="3" fill="#f39a1c"/><rect x="4" y="5" width="14" height="11" fill="#fff"/><g fill="#fff"><rect x="4" y="20" width="3" height="3"/><rect x="9.5" y="20" width="3" height="3"/><rect x="15" y="20" width="3" height="3"/><rect x="4" y="26" width="3" height="3"/><rect x="9.5" y="26" width="3" height="3"/><rect x="15" y="26" width="3" height="3"/></g></svg></div>
</section>

<section class="abs grid">
  <div class="tile selected"><div class="photo" role="img" aria-label="Green hatchback beside a blue hatchback after a colour change wrap"></div><div class="caption"><i></i>COLOUR CHANGE WRAP</div></div>
  <div class="tile"><div class="photo" role="img" aria-label="Van with a full printed wrap"></div><div class="caption"><i></i>PRINTED VEHICLE WRAP</div></div>
  <div class="tile"><div class="photo" role="img" aria-label="Green hatchbacks with tinted windows"></div><div class="caption"><i></i>WINDOW TINT</div></div>
  <div class="tile"><div class="photo" role="img" aria-label="Shop front with window graphics"></div><div class="caption"><i></i>HEADLIGHT TINT</div></div>
  <div class="tile"><div class="photo" role="img" aria-label="White van with business signage"></div><div class="caption"><i></i>VEHICLE SIGNAGE</div></div>
  <div class="tile"><div class="photo" role="img" aria-label="Shop front with signage"></div><div class="caption"><i></i>SHOP SIGNAGE</div></div>
  <div class="tile"><div class="photo" role="img" aria-label="Car with a black vinyl roof"></div><div class="caption"><i></i>ROOF VINYL WRAP</div></div>
  <div class="tile"><div class="photo" role="img" aria-label="Car with a wrapped bonnet"></div><div class="caption"><i></i>BONNET VINYL WRAP</div></div>
  <div class="tile"><div class="photo" role="img" aria-label="Van with a printed wrap"></div><div class="caption"><i></i>CARBON FIBRE VINYL</div></div>
  <div class="tile"><div class="photo" role="img" aria-label="Car bonnet with sticker vinyl"></div><div class="caption"><i></i>STICKERBOMB VINYL</div></div>
  <div class="tile"><div class="photo" role="img" aria-label="White van with protective film"></div><div class="caption"><i></i>CLEAR PROTECTIVE VINYL</div></div>
  <div class="tile"><div class="photo" role="img" aria-label="Green hatchbacks with refurbished wheels"></div><div class="caption"><i></i>WHEEL REFURB</div></div>
</section>

<div class="abs tab" style="left:22px;top:645px"><b>2</b>Input Location &amp; Search</div>
<section class="abs search">
  <div class="field"><small>1</small>Postcode: <span class="input">enter here...</span></div>
  <div class="field"><small>2</small>Distance: <span class="select">5 km</span><span class="search-btn">Search!</span></div>
</section>
<p class="abs hint">Complete step 1 &amp; 2 above to expand panel &amp; continue...</p>

<div class="abs divider"></div>
<section class="abs lower"></section>
<div class="abs why-tab">Why us?</div>

<h2 class="abs heading" style="left:26px;top:786px">Here's why!</h2>
<ul class="abs keypoints">
  <li><svg width="30" height="26" viewBox="0 0 30 26"><path d="M3 14l8 8L27 3" fill="none" stroke="#9cb82a" stroke-width="4" stroke-linecap="round"/></svg>Compare products, locations &amp; Prices.</li>
  <li class="accent"><svg width="30" height="26" viewBox="0 0 30 26"><path d="M3 14l8 8L27 3" fill="none" stroke="#9cb82a" stroke-width="4" stroke-linecap="round"/></svg>Installers throughout the country.</li>
  <li><svg width="30" height="26" viewBox="0 0 30 26"><path d="M3 14l8 8L27 3" fill="none" stroke="#9cb82a" stroke-width="4" stroke-linecap="round"/></svg>Available throughout the country.</li>
  <li class="accent"><svg width="30" height="26" viewBox="0 0 30 26"><path d="M3 14l8 8L27 3" fill="none" stroke="#9cb82a" stroke-width="4" stroke-linecap="round"/></svg>Something else could go here too.</li>
  <li><svg width="30" height="26" viewBox="0 0 30 26"><path d="M3 14l8 8L27 3" fill="none" stroke="#9cb82a" stroke-width="4" stroke-linecap="round"/></svg>Something else could go here too.</li>
</ul>

<div class="abs col-rule"></div>
<h2 class="abs heading" style="left:356px;top:786px">Here's proof!</h2>
<p class="abs proof-note">Say something reassuring here... &amp; say <u>click here</u> to find out more.</p>
<span class="abs label" style="left:348px;top:838px">Before...▼</span>
<span class="abs label" style="left:552px;top:838px">After...▼</span>
<div class="shot" style="left:348px;top:858px"><div class="img">image here...</div><div class="sub">SUBTITLE...</div></div>
<div class="shot" style="left:552px;top:858px"><div class="img">image here...</div><div class="sub">SUBTITLE...</div></div>
<div class="shot" style="left:348px;top:997px"><div class="img">image here...</div><div class="sub">SUBTITLE...</div></div>
<div class="shot" style="left:552px;top:997px"><div class="img">image here...</div><div class="sub">SUBTITLE...</div></div>

<footer class="abs footer">
  <a href="#">HOME</a><a href="#">ABOUT US</a><a href="#">CONTACT US</a><a href="#">BLOG</a>
  <span class="legal">Trademarks property of owners.</span>
</footer>

</body>
</html>
```